The Web Promotion Playbook for Yard & Patio Construction Crews

We need a book cover design that is for a book targeting landscape and outdoor living contractors that helps them grow their business using online marketing.

We run a business focused on this industry so you can see what we do: https://yardcrewgrowthworks.com/

The title is: The Web Promotion Playbook for Yard & Patio Construction Crews

The author is: Trent Varnholm
Some drafts have been done however they're still looking basic and somewhat amateur, we're looking for something that will stand out.

Target Market(s)

Landscape, Hardscape and Outdoor Living Contractors and Business Owners

Industry/Entity Type

Online Marketing

Font styles to use
Serif
Sans Serif

Requirements
Must have
• The part of the title that should stand out the most is the text "Web Promotion Playbook".
Should not have
• The color red

```html
<!DOCTYPE html>
<html lang="en">
<head>
<meta charset="utf-8">
<title>The Web Promotion Playbook for Yard &amp; Patio Construction Crews</title>
<link rel="stylesheet" href="https://fonts.googleapis.com/css2?family=Oswald:wght@400;500&display=swap">
<style>
  :root {
    --backdrop: #e3e8ec;
    --cover-white: #f7f8f8;
    --foliage-dark: #0b1a0e;
    --foliage-mid: #1f5a2c;
    --title-light: #ffffff;
    --title-green: #0b4a1c;
    --rule-grey: #c9cdd0;
  }
  * { margin: 0; padding: 0; box-sizing: border-box; }
  html, body {
    width: 1200px;
    height: 848px;
    overflow: hidden;
    background: var(--backdrop);
  }
  .canvas {
    position: relative;
    width: 1200px;
    height: 848px;
    display: flex;
    align-items: center;
    justify-content: center;
  }
  .book-cover {
    position: relative;
    width: 540px;
    height: 780px;
    background: var(--cover-white);
    overflow: hidden;
    font-family: "Oswald", "Arial Narrow", sans-serif;
    text-transform: uppercase;
  }
  .foliage-photo {
    position: absolute;
    top: 0; left: 0;
    width: 100%;
    height: 51%;
    background:
      radial-gradient(ellipse at 55% 40%, var(--foliage-mid) 0%, rgba(31,90,44,0.5) 35%, transparent 75%),
      var(--foliage-dark);
  }
  .title-block {
    position: absolute;
    top: 296px;
    left: 0;
    width: 100%;
    text-align: center;
    line-height: 1.02;
  }
  .title-lead {
    color: var(--title-light);
    font-weight: 400;
    font-size: 44px;
    letter-spacing: 0.5px;
    transform: scaleX(0.82);
  }
  .title-subject {
    margin-top: 12px;
    color: var(--title-green);
    font-weight: 500;
    font-size: 44px;
    letter-spacing: 0.5px;
    transform: scaleX(0.82);
  }
  .rule-lines {
    position: absolute;
    top: 572px;
    left: 58px;
    width: 250px;
  }
  .rule-lines span {
    display: block;
    height: 1px;
    background: var(--rule-grey);
    margin-bottom: 18px;
  }
  .author {
    position: absolute;
    top: 668px;
    left: 60px;
    width: 250px;
    text-align: center;
    color: var(--title-green);
    font-weight: 500;
    font-size: 30px;
    line-height: 1.1;
    transform: scaleX(0.85);
  }
</style>
</head>
<body>
  <main class="canvas">
    <section class="book-cover">
      <div class="foliage-photo" role="img" aria-label="Close-up photograph of dense dark green leaves"></div>
      <h1 class="title-block">
        <span class="title-lead" style="display:block">The Web Promotion<br>Playbook</span>
        <span class="title-subject" style="display:block">For Yard &amp; Patio<br>Construction Crews</span>
      </h1>
      <div class="rule-lines" aria-hidden="true">
        <span></span><span></span><span></span><span></span>
      </div>
      <p class="author">Trent<br>Varnholm</p>
    </section>
  </main>
</body>
</html>
```